Business Card Design Project

I am looking for a business card design for my custom Audio/Video & Contracting business named Brelvora Systems Inc. We do not currently have a corporate logo so you should not feel constrained to work around an existing design. Your design should be elegant and clean while artistically conveying that we are a technology company. We provide A/V services for the commercial and residential markets and contracting services for residential remodeling and home theater construction. We do not have a particular color that we are looking to design around so feel free to be creative.

To get references of the kind of work that we do and design inspiration please visit the following sites:

http://www.quenlamark.us
www.morvethpro.com
www.feltonbraxa.com

Reason: I think we are getting close on a couple of the designs and want to give additional time to get tweaks done and to resubmit your designs.

Target Market(s)

Most of our clients are very wealthy and have been exposed to premium brand names in every aspect of their lives, (ie. - luxury autos, estate sized homes, fine jewelery and clothes) and your design needs to convey that same level of excellent design that they are used to.

Industry/Entity Type

Residential

Requirements
Should not have
• An extensive use of the color RED.

```html
<!DOCTYPE html>
<html lang="en">
<head>
<meta charset="utf-8">
<title>Brelvora Systems Inc. — Business Card</title>
<link rel="stylesheet" href="https://fonts.googleapis.com/css2?family=Stint+Ultra+Condensed&family=Cormorant+Garamond:ital,wght@1,500&display=swap">
<style>
  :root {
    --page: #f4f8fb;
    --card: #d9e8f5;
    --card-edge: #c3d5e6;
    --brand-blue: #3d80dc;
    --heading-grey: #8c8c8c;
    --body-ink: #3a3a3a;
    --shadow: rgba(40, 60, 90, 0.22);
  }
  * { margin: 0; padding: 0; box-sizing: border-box; }
  html, body {
    width: 1200px;
    height: 900px;
    overflow: hidden;
    background: var(--page);
  }
  .canvas {
    position: relative;
    width: 1200px;
    height: 900px;
  }
  .card {
    position: absolute;
    width: 580px;
    height: 340px;
    background: var(--card);
    border: 1px solid var(--card-edge);
    box-shadow: 3px 4px 10px var(--shadow);
  }
  .card--front { left: 50px; top: 90px; }
  .card--back  { left: 570px; top: 470px; }

  .brand {
    display: flex;
    align-items: center;
    gap: 12px;
    font-family: "Stint Ultra Condensed", serif;
    color: var(--brand-blue);
    white-space: nowrap;
  }
  .brand__dot {
    display: block;
    border-radius: 50%;
    background: var(--heading-grey);
  }
  .card--front .brand {
    position: absolute;
    left: 80px;
    top: 136px;
    font-size: 58px;
    line-height: 1;
  }
  .card--front .brand__dot { width: 26px; height: 26px; }

  .back__title {
    position: absolute;
    left: 0;
    right: 0;
    top: 26px;
    text-align: center;
    font-family: "Stint Ultra Condensed", serif;
    font-size: 50px;
    color: var(--heading-grey);
    letter-spacing: 1px;
  }
  .back__tagline {
    position: absolute;
    left: 40px;
    right: 40px;
    top: 94px;
    text-align: center;
    font-family: "Cormorant Garamond", serif;
    font-style: italic;
    font-weight: 500;
    font-size: 13px;
    line-height: 1.55;
    color: var(--body-ink);
  }
  .contact {
    position: absolute;
    left: 110px;
    top: 148px;
    list-style: none;
    font-family: "Stint Ultra Condensed", serif;
    font-size: 36px;
    line-height: 36px;
    color: var(--brand-blue);
  }
  .contact__row {
    display: flex;
    align-items: flex-end;
    justify-content: flex-end;
    gap: 8px;
  }
  .contact__line {
    display: block;
    width: 160px;
    height: 0;
    margin-bottom: 8px;
    border-bottom: 4px dashed var(--brand-blue);
  }
  .card--back .brand {
    position: absolute;
    right: 30px;
    bottom: 30px;
    font-size: 24px;
    gap: 6px;
  }
  .card--back .brand__dot { width: 12px; height: 12px; }
</style>
</head>
<body>
<main class="canvas">
  <section class="card card--front" aria-label="Card front">
    <div class="brand">
      <span class="brand__dot"></span>
      <span class="brand__name">Brelvora Systems Inc.</span>
    </div>
  </section>

  <section class="card card--back" aria-label="Card back">
    <h1 class="back__title">Audio/Video &amp; Contracting</h1>
    <p class="back__tagline">We provide A/V services for the commercial and residential markets<br>and contracting services for residential remodeling and home theater construction.</p>
    <ul class="contact">
      <li class="contact__row"><span>Tel.</span><span class="contact__line"></span></li>
      <li class="contact__row"><span>Fax</span><span class="contact__line"></span></li>
      <li class="contact__row"><span>e-mail</span><span class="contact__line"></span></li>
      <li class="contact__row"><span>address</span><span class="contact__line"></span></li>
    </ul>
    <div class="brand">
      <span class="brand__dot"></span>
      <span class="brand__name">Brelvora Systems Inc.</span>
    </div>
  </section>
</main>
</body>
</html>
```